Holiday Sale 2026 Graphics for New Year

I want to create 10 social media graphics (new Instagram size 4:5 (1080 x 1350 pixels) focusing on our Holiday Sale Graphics, using any of the pics attached. Use the attached pics, NO RANDOM STOCK PHOTOGRAPHY. For the color scheme of the graphics, they should all be complementary to the product colors in the photos.
You can add any of the photos attached but none are required. You can do some of the graphics in all text. I mainly need BOLD text that says one of the headlines with the pics (10 total):
1. 25% OFF Holiday Sale: New You Starts Now!
2. 25% OFF Everything: New Year, New You
3. 25% OFF Christmas Sale 🎁 Feel Amazing Again!
4. Holiday Treat: 25% OFF Your Favorites
5. 25% OFF All Supplements ✨ New Year Reset!
6. Holiday Magic: 25% OFF Every Supplement
7. 25% OFF to Kickstart Your New Year Goals
8. New Year, New Waistline! 25% OFF Sale
9. Holiday Sale: 25% OFF Everything
10. A Better You Begins With 25% OFF

```html
<!DOCTYPE html>
<html lang="en">
<head>
<meta charset="utf-8">
<title>Holiday Sale Social Graphics</title>
<link href="https://fonts.googleapis.com/css2?family=Anton&family=Bebas+Neue&family=Archivo+Black&display=swap" rel="stylesheet">
<style>
:root{
  --stage:#8e8e8e;
  --paper:#f3f3f3;
  --ink:#1f1f1f;
  --red:#d63838;
  --red-dark:#a82424;
  --purple:#a246b6;
  --blue:#2466d4;
  --blue-light:#3d8ae8;
  --green:#2f9a22;
  --slate:#5e7084;
  --cream:#fbf1e2;
  --white:#ffffff;
}
*{margin:0;padding:0;box-sizing:border-box}
html,body{width:1200px;height:614px;overflow:hidden;background:var(--stage)}
.canvas{position:relative;width:1200px;height:614px}
.panel{position:absolute;width:205px;height:255px;background:var(--paper);overflow:hidden;box-shadow:0 10px 14px rgba(0,0,0,.35)}
.panel > *{position:absolute}
.bg{left:0;top:0;width:205px;height:255px;z-index:0}
.head{font-family:"Anton",sans-serif;line-height:.95;text-transform:uppercase;letter-spacing:.2px;white-space:nowrap;z-index:2}
.light{font-family:"Bebas Neue",sans-serif;line-height:.92;text-transform:uppercase;color:var(--ink);white-space:nowrap;z-index:2}
.sticker{font-family:"Archivo Black",sans-serif;white-space:nowrap;z-index:2}
.pct{display:flex;align-items:center;font-family:"Anton",sans-serif;line-height:.82;color:var(--white);white-space:nowrap;z-index:2}
.pct .n{font-size:var(--s)}
.pct .st{display:flex;flex-direction:column;align-items:center;font-size:calc(var(--s)*.46);margin-left:1px}
.photo-person,.photo-products,.photo-bottle{z-index:1}
.photo-person{background:linear-gradient(180deg,#2a1d19 0%,#3b2b25 30%,#ededed 45%,#dcdcdc 70%,#1c1c1c 100%);border-radius:40px 40px 4px 4px}
.photo-person.dark{background:linear-gradient(180deg,#2a1d19 0%,#3b2b25 30%,#2b2b2b 45%,#444 70%,#151515 100%)}
.photo-products{background:linear-gradient(180deg,#fbfbfb 0%,#ececec 55%,#d9c8e0 80%,#c9d4e6 100%);border-radius:4px}
.photo-bottle{background:linear-gradient(180deg,#fcfcfc 0%,#eeeeee 60%,#c9cfe8 85%,#e8e8e8 100%);border-radius:8px}
.outlined{-webkit-text-stroke:1px var(--blue)}
</style>
</head>
<body>
<main class="canvas">

  <!-- 1 Holiday Sale: New You Starts Now -->
  <section class="panel" style="left:40px;top:31px">
    <svg class="bg" viewBox="0 0 205 255"><path d="M0 145 C60 130 110 165 205 150 L205 255 L0 255Z" fill="var(--red)"/><circle cx="70" cy="140" r="48" fill="none" stroke="#d9a6e0" stroke-width="1.2"/><circle cx="70" cy="140" r="56" fill="none" stroke="#e2c0e8" stroke-width="1"/><rect x="22" y="12" width="82" height="50" rx="8" fill="var(--red)"/></svg>
    <div class="pct" style="left:30px;top:20px;--s:34px"><span class="n">25</span><span class="st"><span>%</span><span>OFF</span></span></div>
    <div class="head" style="left:110px;top:12px;font-size:26px;color:var(--red)">Holiday<br>Sale</div>
    <div class="photo-person" role="img" aria-label="Smiling woman in white cropped sweater" style="left:34px;top:68px;width:78px;height:165px"></div>
    <div class="light" style="left:116px;top:86px;font-size:26px;text-align:right;width:80px">New You<br>Starts<br>Now!</div>
    <div class="photo-products" role="img" aria-label="Row of supplement bottles and sprays" style="left:10px;top:225px;width:188px;height:28px"></div>
  </section>

  <!-- 2 Everything: New Year New You -->
  <section class="panel" style="left:270px;top:31px">
    <svg class="bg" viewBox="0 0 205 255"><path d="M0 0 H205 V80 C150 95 120 145 0 125Z" fill="var(--purple)"/><circle cx="190" cy="195" r="40" fill="none" stroke="#e3c2ea" stroke-width="1.2"/><rect x="20" y="157" width="72" height="58" rx="4" fill="var(--purple)"/><rect x="17" y="147" width="78" height="12" rx="2" fill="var(--purple)"/><path d="M56 147 C40 128 28 140 44 147 M56 147 C72 128 84 140 68 147" fill="none" stroke="var(--purple)" stroke-width="5"/></svg>
    <div class="photo-bottle" role="img" aria-label="Four supplement bottles lined up" style="left:22px;top:28px;width:168px;height:100px"></div>
    <div class="pct" style="left:30px;top:170px;--s:32px"><span class="n">25</span><span class="st"><span>%</span><span>OFF</span></span></div>
    <div class="light" style="left:114px;top:158px;font-size:26px">New Year<br>New You</div>
    <div class="head" style="left:22px;top:210px;font-size:36px;color:var(--purple)">Everything</div>
  </section>

  <!-- 3 Christmas Sale: Feel Amazing Again -->
  <section class="panel" style="left:499px;top:31px">
    <svg class="bg" viewBox="0 0 205 255"><path d="M0 0 H75 L0 72Z" fill="var(--blue)"/><path d="M0 255 V185 C70 170 130 150 205 165 V255Z" fill="var(--blue)"/><circle cx="30" cy="135" r="26" fill="none" stroke="#8fb2e8" stroke-width="1.2"/><circle cx="30" cy="135" r="33" fill="none" stroke="#aac4ee" stroke-width="1"/></svg>
    <div class="pct outlined" style="left:12px;top:14px;--s:36px"><span class="n">25</span><span class="st"><span>%</span><span>OFF</span></span></div>
    <div class="head" style="left:89px;top:12px;font-size:23px;color:var(--blue-light);text-align:center;width:104px">Christmas<br>Sale</div>
    <div class="photo-person dark" role="img" aria-label="Smiling woman in sheer black top" style="left:50px;top:58px;width:74px;height:130px"></div>
    <div class="light" style="left:118px;top:62px;font-size:24px;text-align:right;width:74px">Feel<br>Amazing<br>Again!</div>
    <div class="photo-bottle" role="img" aria-label="Four supplement bottles" style="left:25px;top:152px;width:168px;height:88px"></div>
  </section>

  <!-- 4 Holiday Treat -->
  <section class="panel" style="left:728px;top:31px">
    <svg class="bg" viewBox="0 0 205 255"><path d="M0 88 L205 195 V255 H0Z" fill="var(--green)"/><circle cx="150" cy="140" r="45" fill="none" stroke="#a8c9a3" stroke-width="1.2"/></svg>
    <div class="head" style="left:20px;top:14px;font-size:24px;color:var(--green)">Holiday<br>Treat</div>
    <div class="pct" style="left:104px;top:16px;--s:42px;color:var(--green)"><span class="n">25</span><span class="st"><span>%</span><span>OFF</span></span></div>
    <div class="light" style="left:100px;top:70px;font-size:17px">Your Favorites</div>
    <div class="photo-person dark" role="img" aria-label="Smiling woman in sheer black top" style="left:20px;top:88px;width:82px;height:148px"></div>
    <div class="photo-bottle" role="img" aria-label="Large supplement bottle" style="left:128px;top:130px;width:62px;height:110px"></div>
    <div class="photo-products" role="img" aria-label="Small supplement bottles on counter" style="left:40px;top:228px;width:150px;height:26px"></div>
  </section>

  <!-- 5 Holiday Sale: Everything -->
  <section class="panel" style="left:961px;top:31px">
    <svg class="bg" viewBox="0 0 205 255"><path d="M0 160 L205 125 V255 H0Z" fill="var(--slate)"/><path d="M0 160 L205 125 V120 L0 155Z" fill="var(--blue)"/><path d="M12 82 L32 66 L44 52 L66 58 L90 50 L104 64 L118 80 L104 96 L92 110 L66 104 L44 112 L32 98Z" fill="var(--red)"/></svg>
    <div class="head" style="left:12px;top:12px;font-size:33px;color:var(--slate)">Holiday Sale</div>
    <div class="pct" style="left:34px;top:64px;--s:34px"><span class="n">25</span><span class="st"><span>%</span><span>OFF</span></span></div>
    <div class="light" style="left:15px;top:124px;font-size:24px">Everything</div>
    <div class="photo-person" role="img" aria-label="Smiling woman in white cropped sweater" style="left:104px;top:66px;width:86px;height:170px"></div>
    <div class="photo-products" role="img" aria-label="Row of supplement bottles and sprays" style="left:60px;top:220px;width:140px;height:32px"></div>
  </section>

  <!-- 6 All Supplements: New Year Reset -->
  <section class="panel" style="left:40px;top:318px">
    <svg class="bg" viewBox="0 0 205 255"><circle cx="100" cy="70" r="70" fill="none" stroke="#e1c2e8" stroke-width="1.2"/><circle cx="100" cy="70" r="80" fill="none" stroke="#ead3ee" stroke-width="1"/><rect x="55" y="0" width="93" height="65" fill="var(--purple)"/><path d="M0 175 C60 160 140 150 205 165 V255 H0Z" fill="var(--purple)"/><path d="M22 66 H40 V96 H22 L30 81Z M183 66 H165 V96 H183 L175 81Z" fill="var(--red-dark)"/><rect x="32" y="64" width="141" height="30" fill="var(--red)"/></svg>
    <div class="pct" style="left:66px;top:10px;--s:40px"><span class="n">25</span><span class="st"><span>%</span><span>OFF</span></span></div>
    <div class="head" style="left:32px;top:70px;width:141px;text-align:center;font-size:18px;color:var(--white)">All Supplements</div>
    <div class="light" style="left:0;top:102px;width:205px;text-align:center;font-size:20px">New Year Reset!</div>
    <div class="photo-bottle" role="img" aria-label="Four supplement bottles" style="left:18px;top:135px;width:175px;height:105px"></div>
  </section>

  <!-- 7 Holiday Magic -->
  <section class="panel" style="left:270px;top:318px">
    <svg class="bg" viewBox="0 0 205 255"><path d="M0 0 H205 V90 C140 95 90 110 0 150Z" fill="var(--slate)"/><path d="M0 150 C90 110 140 95 205 90 V98 C140 103 90 118 0 158Z" fill="var(--blue)"/><circle cx="40" cy="230" r="22" fill="none" stroke="#a9b9d8" stroke-width="1"/><path d="M16 88 L34 70 L46 50 L66 60 L90 52 L98 72 L112 90 L98 106 L90 124 L66 116 L46 126 L34 106Z" fill="var(--red)"/></svg>
    <div class="head" style="left:0;top:12px;width:205px;text-align:center;font-size:31px;color:var(--white)">Holiday Magic</div>
    <div class="pct" style="left:28px;top:66px;--s:36px"><span class="n">25</span><span class="st"><span>%</span><span>OFF</span></span></div>
    <div class="light" style="left:15px;top:128px;font-size:40px">Every</div>
    <div class="light" style="left:15px;top:164px;font-size:19px">Supplement</div>
    <div class="photo-person" role="img" aria-label="Smiling woman in white cropped sweater" style="left:102px;top:65px;width:90px;height:170px"></div>
    <div class="photo-products" role="img" aria-label="Row of supplement bottles and sprays" style="left:70px;top:222px;width:130px;height:30px"></div>
  </section>

  <!-- 8 Kickstart Your New Year Goals -->
  <section class="panel" style="left:499px;top:318px">
    <svg class="bg" viewBox="0 0 205 255"><path d="M205 15 C150 25 110 80 110 150 C110 200 130 240 150 255 H205Z" fill="var(--red)"/><path d="M25 62 A38 38 0 1 1 93 62 Q59 48 25 62Z" fill="var(--red)"/><circle cx="160" cy="35" r="30" fill="none" stroke="#f0b5b5" stroke-width="1"/></svg>
    <div class="pct" style="left:31px;top:22px;--s:31px"><span class="n">25</span><span class="st"><span>%</span><span>OFF</span></span></div>
    <div class="light" style="left:0;top:80px;width:118px;text-align:center;font-size:14px">To</div>
    <div class="head" style="left:0;top:92px;width:118px;text-align:center;font-size:25px;color:var(--red)">Kickstart</div>
    <div class="light" style="left:0;top:124px;width:118px;text-align:center;font-size:22px">Your<br>New Year<br>Goals</div>
    <div class="photo-person dark" role="img" aria-label="Smiling woman in sheer black top" style="left:114px;top:78px;width:86px;height:160px"></div>
    <div class="photo-bottle" role="img" aria-label="Four supplement bottles" style="left:15px;top:194px;width:88px;height:48px"></div>
  </section>

  <!-- 9 New Year New Waistline -->
  <section class="panel" style="left:728px;top:318px">
    <svg class="bg" viewBox="0 0 205 255"><path d="M0 0 H205 V70 C150 60 120 140 205 165 V175 C110 150 140 75 0 75Z" fill="var(--blue)"/><path d="M205 165 C120 140 150 60 205 70 Z" fill="var(--blue-light)" opacity=".5"/><circle cx="20" cy="235" r="20" fill="none" stroke="#9fbce8" stroke-width="1"/><rect x="24" y="82" width="84" height="72" rx="8" fill="var(--cream)"/><path d="M20 152 L100 140 L102 172 L22 178Z" fill="var(--red)"/></svg>
    <div class="light" style="left:16px;top:12px;font-size:31px;color:var(--white);line-height:.9">New Year<br>New Waistline!</div>
    <div class="sticker" style="left:28px;top:90px;width:78px;text-align:center;font-size:22px;line-height:.95;color:var(--red)">25%<br>OFF</div>
    <div class="sticker" style="left:26px;top:152px;font-size:13px;color:var(--white)">SALE!</div>
    <div class="photo-person" role="img" aria-label="Smiling woman in white cropped sweater" style="left:100px;top:64px;width:86px;height:174px"></div>
    <div class="photo-products" role="img" aria-label="Row of supplement bottles and sprays" style="left:30px;top:222px;width:170px;height:30px"></div>
  </section>

  <!-- 10 A Better You Begins With -->
  <section class="panel" style="left:961px;top:318px">
    <svg class="bg" viewBox="0 0 205 255"><path d="M0 200 C60 150 140 135 205 150 V255 H0Z" fill="var(--green)"/><circle cx="150" cy="140" r="34" fill="none" stroke="#a9caa3" stroke-width="1.2"/><path d="M14 14 H195 V22 A4 4 0 0 0 195 30 V36 A4 4 0 0 0 195 44 V52 H14 V44 A4 4 0 0 0 14 36 V30 A4 4 0 0 0 14 22Z" fill="var(--green)"/><rect x="115" y="68" width="75" height="52" rx="3" fill="var(--green)"/><path d="M152 68 C138 50 126 60 142 68 M152 68 C166 50 178 60 162 68" fill="none" stroke="var(--green)" stroke-width="5"/></svg>
    <div class="head" style="left:14px;top:18px;width:181px;text-align:center;font-size:28px;color:var(--white)">A Better You</div>
    <div class="light" style="left:16px;top:56px;font-size:23px">Begins With</div>
    <div class="pct" style="left:126px;top:78px;--s:32px"><span class="n">25</span><span class="st"><span>%</span><span>OFF</span></span></div>
    <div class="photo-person dark" role="img" aria-label="Smiling woman in sheer black top" style="left:22px;top:80px;width:64px;height:104px"></div>
    <div class="photo-bottle" role="img" aria-label="Four supplement bottles" style="left:20px;top:145px;width:172px;height:95px"></div>
  </section>

</main>
</body>
</html>
```